Orvel Prime - Letter Head

My company is a residential and commercial cleaning company , which is located in Abu Dhabi, UAE.
I am looking for a creative letterhead reflects the professional and reflects professionalism and send the feeling of relax and comfort.
The color which will be used it has to be selected carefully in prospective of colors psychological effects, so every color to be used should be for a reason.
Also, reflecting my company colors in an attractive way.
Regarding the information which it should contains, it has to show the address, contacts , telephones an, email address and website.
Also, my company logo is attached
Residential

```html
<!DOCTYPE html>
<html lang="en">
<head>
<meta charset="utf-8">
<title>Orvel Prime - Letterhead</title>
<link href="https://fonts.googleapis.com/css2?family=Open+Sans:wght@400;700&display=swap" rel="stylesheet">
<style>
  :root {
    --backdrop: #e9eaec;
    --paper: #ffffff;
    --brand-blue: #1d75b8;
    --brand-green: #9ccb3b;
    --ink: #555a60;
    --faint-circle: #dfeec0;
  }
  * { margin: 0; padding: 0; box-sizing: border-box; }
  html, body {
    width: 1200px;
    height: 1000px;
    overflow: hidden;
    background: var(--backdrop);
    font-family: "Open Sans", Arial, sans-serif;
  }
  .letterhead {
    position: absolute;
    left: 268px;
    top: 30px;
    width: 664px;
    height: 940px;
    background: var(--paper);
    box-shadow: 0 2px 10px rgba(0, 0, 0, 0.12);
    overflow: hidden;
  }
  .brand {
    position: absolute;
    left: 40px;
    top: 40px;
    display: flex;
    align-items: center;
    gap: 10px;
  }
  .brand-dot {
    width: 34px;
    height: 34px;
    border-radius: 50%;
    background: var(--brand-green);
  }
  .brand-name {
    font-size: 26px;
    font-weight: 700;
    color: var(--brand-blue);
    letter-spacing: 0.2px;
  }
  .corner-mark {
    position: absolute;
    right: 22px;
    bottom: 80px;
    width: 110px;
    height: 110px;
    border-radius: 50%;
    border: 3px solid var(--faint-circle);
  }
  .footer-details {
    position: absolute;
    left: 250px;
    right: 40px;
    bottom: 36px;
    display: flex;
    justify-content: space-between;
    font-size: 8.5px;
    line-height: 1.45;
    color: var(--ink);
  }
  .footer-bands {
    position: absolute;
    left: 0;
    bottom: 0;
    width: 664px;
    height: 30px;
  }
</style>
</head>
<body>
  <main class="letterhead">
    <header class="brand">
      <span class="brand-dot"></span>
      <span class="brand-name">Orvel Prime</span>
    </header>

    <div class="corner-mark"></div>

    <footer class="footer-details">
      <address class="detail-address" style="font-style: normal;">
        Al - Noor Court, Second Floor,<br>
        Unit 218, Abu Dhabi, UAE 54321
      </address>
      <div class="detail-phones">
        Tel: 555 010 2468<br>
        Fax: 555 0102469
      </div>
      <div class="detail-online">
        Email: hello@orvelprime.example<br>
        Web: www.orvelprime.example
      </div>
    </footer>

    <svg class="footer-bands" viewBox="0 0 664 30" aria-hidden="true">
      <path d="M528 2 H664 V16 H520 V10 Q520 2 528 2 Z" fill="var(--brand-green)"/>
      <rect x="0" y="16" width="520" height="14" fill="var(--brand-blue)"/>
    </svg>
  </main>
</body>
</html>
```